FinTech company looking to revamp and expand client-facing interface for our financial models

Halvern Ledgerworks currently has a very simple website that allows clients to interact with our financial models. We are looking to completely redesign the current site and add several extra pages to provide extra functionality. We want the design to have a modern, slick feel, that will work on both a desktop or a tablet. It should be straightforward for clients to move between different pages at any time, and clear from the layout how to interact with the more advanced features. We have included screenshots of existing pages in the attached design brief, as well as sketches of the functionality required by the new pages, but can't provide a direct link to the current site.
Target Market(s)
Professional investors that will be paying to access the interface
Industry/Entity Type
Finance
Number of Pages Required
4 page
Colors
Designer to choose colors to be used in the design.
Look and feel
Each slider illustrates characteristics of the customer's brand and the style your logo design should communicate.

```html
<!DOCTYPE html>
<html lang="en">
<head>
<meta charset="utf-8">
<title>Halvern Ledgerworks — Model Dashboard</title>
<link href="https://fonts.googleapis.com/css2?family=Fira+Sans:wght@400;500;700&display=swap" rel="stylesheet">
<style>
:root{
  --ink:#111;
  --text:#333;
  --muted:#666;
  --line:#cfcfcf;
  --rule:#444;
  --accent:#0a8fc4;
  --up:#5cc21a;
  --down:#e01010;
  --footer:#333;
  --footer-text:#fff;
  --series-a:#1e2a78;
  --series-b:#5a9a3a;
  --series-c:#6fa3a0;
  --grid:#e3e3e3;
}
*{box-sizing:border-box;margin:0;padding:0}
html,body{width:1200px;height:979px;overflow:hidden;background:#fff}
body{position:relative;font-family:"Fira Sans",Arial,sans-serif;color:var(--text)}
.abs{position:absolute;white-space:nowrap}

.site-header{position:absolute;left:0;top:0;width:1200px;height:56px;border:1px solid var(--line);background:#fff}
.brand{left:65px;top:14px;font-weight:700;font-size:22px;color:var(--ink)}
.range-tab{top:17px;height:24px;line-height:24px;font-size:11px;color:var(--muted);text-align:center}
.range-tab.active{border:1px solid var(--accent);color:var(--accent);width:55px}
.main-nav a{position:absolute;top:21px;font-size:11.5px;color:var(--muted);text-decoration:none;transform:translateX(-50%)}
.main-nav a.current{color:var(--accent)}

.sidebar{position:absolute;left:124px;top:56px;width:292px;height:774px;border:1px solid var(--line);border-top:none}
.search{position:absolute;left:29px;top:26px;width:197px;height:23px;border-bottom:1px solid var(--line);font-size:11.5px;color:#aaa}
.search svg{position:absolute;left:0;top:1px}
.search span{position:absolute;left:23px;top:2px}
.model-item{position:absolute;left:0;width:290px;height:63px;border-bottom:1px solid var(--line)}
.model-item.selected{background:#000;color:#fff}
.model-name{left:29px;top:9px;font-size:15px}
.model-change{left:217px;top:11px;font-size:11.5px}
.model-change svg{vertical-align:-1px;margin-right:5px}
.q{font-size:11.5px}
.up{color:var(--up)}
.down{color:var(--down)}

.content{position:absolute;left:416px;top:56px;width:658px;height:774px;border-right:1px solid var(--line)}
.content-top{position:absolute;left:0;top:24px;width:657px;border-top:1px solid var(--line)}
.model-title{position:absolute;left:454px;top:150px;font-size:22px;color:var(--text)}
.title-rule{position:absolute;left:452px;top:184px;width:482px;border-top:1px solid var(--rule)}

.stats{position:absolute;left:452px;top:226px;width:357px;border-collapse:collapse;font-size:11.5px}
.stats th{font-weight:400;color:var(--ink);height:26px;text-align:center;border-bottom:1px solid var(--rule)}
.stats td{height:24px;text-align:center;border-bottom:1px solid var(--line);color:var(--text)}
.stats th:first-child,.stats td:first-child{text-align:left;padding-left:3px;width:96px}

.chart-label{position:absolute;left:452px;width:107px;font-size:12px;border-bottom:1px solid var(--line);padding-bottom:4px;padding-left:3px}
.chart{position:absolute;left:452px;font-family:"Fira Sans",Arial,sans-serif}
.chart text{font-size:6.5px;fill:#333}

.site-footer{position:absolute;left:0;top:830px;width:1200px;height:149px;background:var(--footer);color:var(--footer-text)}
.footer-col{position:absolute;top:37px;font-size:10.5px;line-height:19px}
.footer-brand{position:absolute;right:130px;top:56px;text-align:right}
.footer-brand strong{display:block;font-size:22px;font-weight:700;line-height:26px}
.footer-brand small{font-size:10.5px}
</style>
</head>
<body>

<header class="site-header">
  <div class="abs brand">Halvern</div>
  <div class="abs range-tab active" style="left:165px">250D</div>
  <div class="abs range-tab" style="left:245px;width:20px">83D</div>
  <div class="abs range-tab" style="left:307px;width:20px">42D</div>
  <nav class="main-nav">
    <a class="current" style="left:839px">Dashboard</a>
    <a style="left:925px">Models</a>
    <a style="left:1012px">Sensitives</a>
    <a style="left:1098px">Portfolio</a>
  </nav>
</header>

<aside class="sidebar">
  <div class="search">
    <svg width="15" height="15" viewBox="0 0 15 15"><circle cx="6" cy="6" r="5" fill="none" stroke="#aaa" stroke-width="1.2"/><line x1="9.6" y1="9.6" x2="14" y2="14" stroke="#aaa" stroke-width="1.2"/></svg>
    <span>Search here</span>
  </div>
  <div class="model-item selected" style="top:65px">
    <div class="abs model-name">Model 1</div>
    <div class="abs model-change up"><svg width="11" height="11" viewBox="0 0 11 11"><path d="M1 10 L5.5 1 L10 10" fill="none" stroke="var(--up)" stroke-width="2"/></svg>2.3%</div>
    <div class="abs q up" style="left:31px;top:40px">Q1 : 18</div>
    <div class="abs q up" style="left:97px;top:40px">Q2 : 2</div>
    <div class="abs q down" style="left:157px;top:40px">Q3 : -5</div>
    <div class="abs q down" style="left:220px;top:40px">Q3 : -5</div>
  </div>
  <div class="model-item" style="top:128px">
    <div class="abs model-name">Model 2</div>
    <div class="abs model-change down"><svg width="11" height="11" viewBox="0 0 11 11"><path d="M1 1 L5.5 10 L10 1" fill="none" stroke="var(--down)" stroke-width="2"/></svg>-1.3%</div>
    <div class="abs q down" style="left:31px;top:40px">Q1 : -9</div>
    <div class="abs q down" style="left:97px;top:40px">Q2 : 2</div>
    <div class="abs q up" style="left:157px;top:40px">Q3 : 25</div>
    <div class="abs q down" style="left:220px;top:40px">Q3 : 2.3</div>
  </div>
</aside>

<main class="content">
  <div class="content-top"></div>
</main>

<h1 class="model-title" style="font-weight:400">Model 1</h1>
<div class="abs q up" style="left:638px;top:161px">Q1 : 18</div>
<div class="abs q up" style="left:704px;top:161px">Q2 : 2</div>
<div class="abs q down" style="left:764px;top:161px">Q3 : -5</div>
<div class="abs q down" style="left:827px;top:161px">Q3 : -5</div>
<div class="title-rule"></div>

<table class="stats">
  <thead><tr><th>Id</th><th>Stat1</th><th>Stat2</th><th>Stat3</th><th>Stat4</th></tr></thead>
  <tbody>
    <tr><td>Factor 1</td><td>2.3</td><td>12</td><td>14.5</td><td>35</td></tr>
    <tr><td>Factor 2</td><td>5</td><td>3</td><td>1</td><td>3</td></tr>
  </tbody>
</table>

<div class="chart-label" style="top:349px">Factor 1</div>
<svg class="chart" style="top:380px" width="570" height="175" viewBox="452 380 570 175">
  <g stroke="var(--grid)" stroke-width="0.6">
    <line x1="466" y1="399" x2="1011" y2="399"/><line x1="466" y1="421.5" x2="1011" y2="421.5"/>
    <line x1="466" y1="444" x2="1011" y2="444"/><line x1="466" y1="466.5" x2="1011" y2="466.5"/>
    <line x1="466" y1="489" x2="1011" y2="489"/><line x1="466" y1="511.5" x2="1011" y2="511.5"/>
    <line x1="466" y1="534" x2="1011" y2="534"/>
  </g>
  <g stroke="#d2d2d2" stroke-width="0.6">
    <line x1="497" y1="383" x2="497" y2="541"/><line x1="545" y1="383" x2="545" y2="541"/>
    <line x1="591" y1="383" x2="591" y2="541"/><line x1="638" y1="383" x2="638" y2="541"/>
    <line x1="684" y1="383" x2="684" y2="541"/><line x1="732" y1="383" x2="732" y2="541"/>
    <line x1="779" y1="383" x2="779" y2="541"/><line x1="822" y1="383" x2="822" y2="541"/>
    <line x1="869" y1="383" x2="869" y2="541"/><line x1="916" y1="383" x2="916" y2="541"/>
    <line x1="963" y1="383" x2="963" y2="541"/><line x1="1009" y1="383" x2="1009" y2="541"/>
  </g>
  <line x1="466" y1="383" x2="466" y2="541" stroke="#999" stroke-width="0.6"/>
  <line x1="466" y1="541" x2="1011" y2="541" stroke="#999" stroke-width="0.6"/>
  <polyline fill="none" stroke="var(--series-b)" stroke-width="0.8" points="466,405 470,410 474,406 478,424 481,418 486,430 490,425 495,428 500,423 506,430 512,425 518,432 524,420 530,428 536,422 542,418 548,425 553,432 558,428 565,432 572,426 578,430 584,424 590,428 595,422 601,432 606,448 611,455 616,446 621,452 627,462 632,455 637,470 642,458 648,466 653,462 658,472 663,468 668,476 673,480 678,474 684,478 690,488 696,494 702,492 708,498 714,494 720,502 726,505 732,500 738,496 744,492 750,496 756,490 762,494 768,488 774,495 780,492 786,488 792,496 798,490 804,486 808,482 812,490 818,494 824,492 830,488 836,484 842,488 848,482 854,486 860,482 866,488 872,492 878,496 884,494 890,500 896,506 902,508 908,512 914,514 920,512 926,518 932,516 938,524 944,528 950,526 956,524 962,528 968,526 974,524 980,522 986,520 992,522 998,519 1004,518 1010,519"/>
  <polyline fill="none" stroke="var(--series-a)" stroke-width="0.8" points="466,400 470,403 474,399 478,412 482,408 486,421 490,415 495,411 500,418 506,412 512,416 518,410 523,416 528,414 534,418 540,414 545,420 550,424 556,426 562,421 568,428 574,424 580,428 586,426 591,430 596,434 601,440 606,446 611,440 616,448 622,444 628,440 632,446 637,442 642,440 647,444 652,438 658,442 663,446 668,444 673,452 678,456 684,460 690,466 696,476 702,484 708,486 714,484 720,480 726,482 732,478 738,482 744,478 750,482 756,476 762,480 768,478 774,482 780,478 786,474 790,470 795,476 800,480 806,484 812,480 818,482 824,486 830,484 836,488 842,486 848,490 854,488 860,494 866,494 872,498 878,500 884,504 890,506 896,508 902,510 908,512 914,510 920,514 926,518 932,522 938,520 944,520 950,518 956,520 962,520 968,522 974,520 980,521 986,522 992,520 998,522 1004,522 1010,523"/>
  <g text-anchor="end">
    <text x="463" y="401">50</text><text x="463" y="423.5">45</text><text x="463" y="446">40</text>
    <text x="463" y="468.5">35</text><text x="463" y="491">30</text><text x="463" y="513.5">25</text>
    <text x="463" y="536">20</text>
  </g>
  <g text-anchor="middle">
    <text x="497" y="551">Aug 2018</text><text x="545" y="551">Sep 2018</text><text x="591" y="551">Oct 2018</text>
    <text x="638" y="551">Nov 2018</text><text x="684" y="551">Dec 2018</text><text x="732" y="551">Jan 2019</text>
    <text x="779" y="551">Feb 2019</text><text x="822" y="551">Mar 2019</text><text x="869" y="551">Apr 2019</text>
    <text x="916" y="551">May 2019</text><text x="963" y="551">Jun 2019</text><text x="1001" y="551">Jul 2019</text>
  </g>
</svg>

<div class="chart-label" style="top:591px">Factor 2</div>
<svg class="chart" style="top:624px" width="570" height="180" viewBox="452 624 570 180">
  <g stroke="var(--grid)" stroke-width="0.6">
    <line x1="469" y1="652" x2="1008" y2="652"/><line x1="469" y1="693.3" x2="1008" y2="693.3"/>
    <line x1="469" y1="734.7" x2="1008" y2="734.7"/><line x1="469" y1="776" x2="1008" y2="776"/>
  </g>
  <g stroke="#d2d2d2" stroke-width="0.6">
    <line x1="501" y1="636" x2="501" y2="791"/><line x1="548" y1="636" x2="548" y2="791"/>
    <line x1="594" y1="636" x2="594" y2="791"/><line x1="640" y1="636" x2="640" y2="791"/>
    <line x1="686" y1="636" x2="686" y2="791"/><line x1="732" y1="636" x2="732" y2="791"/>
    <line x1="779" y1="636" x2="779" y2="791"/><line x1="821" y1="636" x2="821" y2="791"/>
    <line x1="868" y1="636" x2="868" y2="791"/><line x1="913" y1="636" x2="913" y2="791"/>
    <line x1="960" y1="636" x2="960" y2="791"/><line x1="1006" y1="636" x2="1006" y2="791"/>
  </g>
  <line x1="469" y1="636" x2="469" y2="791" stroke="#999" stroke-width="0.6"/>
  <line x1="469" y1="791" x2="1008" y2="791" stroke="#999" stroke-width="0.6"/>
  <polyline fill="none" stroke="var(--series-c)" stroke-width="0.8" points="469,730 474,723 479,725 483,752 488,740 493,742 498,732 502,734 507,731 512,745 516,757 520,758 524,734 530,734 536,728 542,726 546,731 550,746 556,742 562,746 568,744 574,748 580,742 584,760 589,766 594,764 599,768 604,760 608,766 614,763 619,768 624,772 628,778 632,774 636,760 640,742 645,740 648,729 652,727 654,744 660,738 664,742 670,736 674,741 677,735 682,744 688,736 694,736 698,731 704,727 708,712 713,708 718,710 722,716 726,700 730,702 734,694 740,690 744,688 748,687 752,676 756,690 760,680 764,685 770,690 774,707 778,688 782,689 788,680 792,691 796,682 802,688 808,686 812,668 818,664 824,661 828,666 830,690 834,684 840,688 844,680 848,674 852,677 856,686 860,683 864,692 868,702 872,688 878,686 882,682 886,690 890,684 896,682 900,690 904,680 908,676 912,676 918,680 924,682 930,678 936,676 942,680 948,672 952,676 956,668 960,672 966,676 972,670 978,674 982,668 986,658 990,654 994,658 998,654 1002,660 1006,650"/>
  <g text-anchor="end">
    <text x="467" y="654">30</text><text x="467" y="695.3">25</text>
    <text x="467" y="736.7">20</text><text x="467" y="778">15</text>
  </g>
  <g text-anchor="middle">
    <text x="501" y="634">Aug 2018</text><text x="548" y="634">Sep 2018</text><text x="594" y="634">Oct 2018</text>
    <text x="640" y="634">Nov 2018</text><text x="686" y="634">Dec 2018</text><text x="732" y="634">Jan 2019</text>
    <text x="779" y="634">Feb 2019</text><text x="821" y="634">Mar 2019</text><text x="868" y="634">Apr 2019</text>
    <text x="913" y="634">May 2019</text><text x="960" y="634">Jun 2019</text><text x="998" y="634">Jul 2019</text>
    <text x="501" y="801">Aug 2018</text><text x="548" y="801">Sep 2018</text><text x="594" y="801">Oct 2018</text>
    <text x="640" y="801">Nov 2018</text><text x="686" y="801">Dec 2018</text><text x="732" y="801">Jan 2019</text>
    <text x="779" y="801">Feb 2019</text><text x="821" y="801">Mar 2019</text><text x="868" y="801">Apr 2019</text>
    <text x="913" y="801">May 2019</text><text x="960" y="801">Jun 2019</text><text x="998" y="801">Jul 2019</text>
  </g>
</svg>

<footer class="site-footer">
  <div class="footer-col" style="left:188px">Dashboard<br>Portfolio</div>
  <div class="footer-col" style="left:309px">Models<br>&nbsp;Q1<br>&nbsp;Q2</div>
  <div class="footer-col" style="left:435px">Sensitives<br>&nbsp;Q1<br>&nbsp;Q2</div>
  <div class="footer-col" style="left:581px">How to do?<br>Help<br>Contact</div>
  <div class="footer-col" style="left:722px">About<br>Media</div>
  <div class="footer-brand"><strong>Halvern</strong><small>All rights Reserved</small></div>
</footer>

</body>
</html>
```